Labor Day Sale Website Banner For High End Jewelry Website

We need a banner for our website (brindlyx.com) for a Labor Day Sale. The banner should be a size 1187 × 400. I have included a few pieces of jewelry to be included in the banner (do not need to use all, can use just some). The banner should say:
"Labor Day Sale"
"Save 15% on Everything!"
Use Promo Code: HALCYON

Target Market(s)

Affluent Female Consumers

Industry/Entity Type

Jewelry

Colors

Designer to choose colors to be used in the design.

```html
<!DOCTYPE html>
<html lang="en">
<head>
<meta charset="UTF-8">
<title>Labor Day Sale Banner</title>
<link href="https://fonts.googleapis.com/css2?family=Cinzel:wght@400;700&family=Oswald:wght@700&display=swap" rel="stylesheet">
<style>
  :root {
    --page-bg: #e6e6e6;
    --banner-black: #0c0c0c;
    --banner-charcoal: #262626;
    --gold-light: #f6de8a;
    --gold: #d3a43a;
    --gold-deep: #8a6418;
    --silver-light: #ffffff;
    --silver: #b9b9b9;
    --text-white: #f2f2f2;
    --photo-white: #ffffff;
    --photo-cream: #f3efe6;
  }
  * { margin: 0; padding: 0; box-sizing: border-box; }
  html, body { width: 1200px; height: 668px; overflow: hidden; background: var(--page-bg); }
  .canvas { position: relative; width: 1200px; height: 668px; }

  .banner {
    position: absolute; left: 74px; top: 124px; width: 1057px; height: 368px;
    overflow: hidden;
    background:
      radial-gradient(ellipse at 62% 30%, var(--banner-charcoal) 0%, rgba(20,20,20,0.6) 40%, transparent 75%),
      var(--banner-black);
  }

  .bracelet-photo {
    position: absolute; left: 40px; top: 44px; width: 350px; height: 130px;
    background: linear-gradient(180deg, rgba(211,164,58,0.55), rgba(138,100,24,0.35));
  }

  .gold-arc { position: absolute; left: 0; top: 0; }

  .offer { position: absolute; left: 100px; top: 208px; }
  .offer-figure {
    font-family: "Oswald", sans-serif; font-weight: 700; font-size: 118px; line-height: 1;
    letter-spacing: -4px;
    background: linear-gradient(180deg, var(--gold-light), var(--gold) 50%, var(--gold-deep));
    -webkit-background-clip: text; background-clip: text; color: transparent;
    text-shadow: 4px 4px 0 rgba(90,60,10,0.35);
  }
  .offer-figure .percent { font-size: 70px; vertical-align: top; }
  .offer-terms {
    position: absolute; left: 122px; top: 70px; width: 200px;
    font-family: "Cinzel", serif; font-size: 14px; line-height: 16px; color: var(--text-white);
  }
  .promo-code { color: var(--gold); font-weight: 700; }

  .headline {
    position: absolute; left: 548px; top: 54px;
    font-family: "Cinzel", serif; font-weight: 400; font-size: 55px; line-height: 1; white-space: nowrap;
  }
  .headline .silver {
    background: linear-gradient(180deg, var(--silver-light), var(--silver) 60%, #ececec);
    -webkit-background-clip: text; background-clip: text; color: transparent;
  }
  .headline .gold {
    font-size: 68px;
    background: linear-gradient(180deg, var(--gold-light), var(--gold) 60%, var(--gold-deep));
    -webkit-background-clip: text; background-clip: text; color: transparent;
  }
  .headline-rule {
    position: absolute; left: 556px; top: 131px; width: 472px; height: 2px;
    background: linear-gradient(90deg, transparent, var(--silver) 20%, var(--silver-light) 50%, var(--silver) 80%, transparent);
  }

  .product-card {
    position: absolute; width: 138px; height: 142px; padding: 8px 8px 32px;
    background: linear-gradient(160deg, var(--gold-light), var(--gold) 55%, var(--gold-deep));
    box-shadow: 0 60px 0 -10px rgba(0,0,0,0.55);
  }
  .product-photo {
    width: 100%; height: 100%;
    background: linear-gradient(180deg, var(--photo-white), var(--photo-cream));
  }
  .card-earrings { left: 582px; top: 182px; transform: rotate(-8deg); }
  .card-pendant { left: 716px; top: 168px; width: 112px; }
  .card-ring { left: 834px; top: 182px; transform: rotate(8deg); }
</style>
</head>
<body>
<div class="canvas">
  <section class="banner" aria-label="Labor Day Sale banner">
    <div class="bracelet-photo" role="img" aria-label="Photo of a gold and diamond twisted link bracelet"></div>

    <svg class="gold-arc" width="1057" height="368" viewBox="0 0 1057 368" aria-hidden="true">
      <defs>
        <linearGradient id="arcGold" x1="0" y1="0" x2="0" y2="1">
          <stop offset="0" stop-color="#f6de8a"/>
          <stop offset="0.5" stop-color="#d3a43a"/>
          <stop offset="1" stop-color="#8a6418"/>
        </linearGradient>
      </defs>
      <path d="M478 100 C 510 180, 480 300, 392 368 L 404 368 C 490 300, 520 180, 478 100 Z" fill="url(#arcGold)"/>
    </svg>

    <div class="offer">
      <div class="offer-figure">15<span class="percent">%</span></div>
      <p class="offer-terms">on Everything!<br>Use Promo Code:<br><span class="promo-code">HALCYON</span></p>
    </div>

    <h1 class="headline"><span class="silver">Labor Day</span> <span class="gold">Sale</span></h1>
    <div class="headline-rule"></div>

    <figure class="product-card card-earrings">
      <div class="product-photo" role="img" aria-label="Photo of gold button earrings"></div>
    </figure>
    <figure class="product-card card-pendant">
      <div class="product-photo" role="img" aria-label="Photo of a gold and diamond pendant"></div>
    </figure>
    <figure class="product-card card-ring">
      <div class="product-photo" role="img" aria-label="Photo of a gold ring with a purple stone"></div>
    </figure>
  </section>
</div>
</body>
</html>
```